Make it POP! Label design for Australian Skin Care range

I want to see elegance, femininity, luxury, glamour.
Design needs to compliment existing logo in style and colours; turquoise and silver (see file). text required (see file)
There are 5 different products with different text - same design required.
Please see file attached for the containers the labels will be applied to.

Target Market(s)

women over 35

Industry/Entity Type

Skin Care Product

Font styles to use
Sans Serif

Colors
33b8a4

Requirements
Must have
• Design in Turquoise and silver
• Sans Serif fonts, compliment existing logo (see file)
• contain text exactly as written (see file)
Nice to have
• Feminine, flowing lines/ shapes
Should not have
• Black, nothing bold or masculine. Nothing that looks clinical or medical

```html
<!DOCTYPE html>
<html lang="en">
<head>
<meta charset="utf-8">
<title>Elora Bloom – Native Hydrating Serum Label</title>
<link rel="stylesheet" href="https://fonts.googleapis.com/css2?family=Montserrat:wght@300;400;500;600&family=Quicksand:wght@400;500&display=swap">
<style>
  :root {
    --teal: #33b8a4;
    --teal-deep: #1c9a93;
    --teal-dark: #138683;
    --teal-soft: #8fd3cf;
    --teal-mist: #c5e8e6;
    --silver: #b9bcbe;
    --silver-light: #e4e6e7;
    --label-white: #f4f5f5;
    --page: #ffffff;
  }
  * { margin: 0; padding: 0; box-sizing: border-box; }
  html, body { width: 900px; height: 1200px; overflow: hidden; background: var(--page); }
  .label {
    position: relative;
    width: 900px;
    height: 1200px;
    overflow: hidden;
    background: linear-gradient(90deg, var(--label-white) 0%, #ffffff 45%, #e9ebeb 100%);
    font-family: "Quicksand", sans-serif;
  }
  .label-art { position: absolute; inset: 0; }
  .brand {
    position: absolute; top: 70px; left: 0; right: 0;
    display: flex; flex-direction: column; align-items: center;
  }
  .brand-mark {
    width: 170px; height: 170px; border-radius: 50%;
    background: radial-gradient(circle at 40% 35%, #4cc6bd, var(--teal-deep));
    box-shadow: 0 0 0 5px var(--silver-light);
  }
  .brand-name {
    margin-top: 40px;
    font-family: "Montserrat", sans-serif; font-weight: 400;
    font-size: 30px; letter-spacing: 18px; color: var(--silver);
    padding-left: 18px;
  }
  .tagline {
    margin-top: 26px; text-align: center;
    font-size: 27px; line-height: 36px; color: var(--teal);
  }
  .product-title {
    position: absolute; top: 640px; left: 0; right: 0; text-align: center;
    font-family: "Montserrat", sans-serif; font-weight: 600;
    font-size: 52px; line-height: 72px; color: var(--silver-light);
    letter-spacing: 1px;
  }
  .ingredients {
    position: absolute; top: 900px; left: 0; right: 0; text-align: center;
    color: var(--teal);
  }
  .ingredients-lead { font-size: 32px; }
  .ingredients-list { margin-top: 8px; font-size: 32px; }
  .ingredients-list .dot { margin: 0 14px; }
  .skin-type {
    display: inline-block; margin-top: 24px;
    background: var(--teal); color: #ffffff;
    font-size: 28px; padding: 6px 30px 8px; border-radius: 30px;
  }
  .base-band {
    position: absolute; left: 0; right: 0; bottom: 0; height: 92px;
    background: linear-gradient(90deg, var(--teal) 0%, #47c3b9 40%, var(--teal-deep) 100%);
    border-top: 5px solid var(--silver-light);
  }
  .net-weight {
    position: absolute; left: 24px; bottom: 22px;
    font-family: "Montserrat", sans-serif; color: #ffffff;
    font-size: 18px; font-weight: 300;
  }
  .net-weight strong { font-size: 36px; font-weight: 500; }
  .vegan-badge {
    position: absolute; right: 22px; bottom: 14px;
    width: 124px; height: 124px; border-radius: 50%;
    background: var(--teal-deep); border: 5px solid var(--silver-light);
  }
</style>
</head>
<body>
  <div class="label">
    <svg class="label-art" viewBox="0 0 900 1200" width="900" height="1200" aria-hidden="true">
      <defs>
        <linearGradient id="bandMain" x1="0" y1="0" x2="1" y2="0">
          <stop offset="0" stop-color="#1c9a93"/>
          <stop offset="0.5" stop-color="#12807e"/>
          <stop offset="1" stop-color="#1c9a93"/>
        </linearGradient>
      </defs>
      <path d="M0,440 C160,560 480,640 900,690 L900,760 C520,700 200,640 0,600 Z" fill="#c5e8e6"/>
      <path d="M0,500 C200,600 520,660 900,710 L900,780 C520,740 220,700 0,680 Z" fill="#8fd3cf"/>
      <path d="M0,580 C260,640 560,690 900,730 L900,850 C600,870 300,890 0,910 Z" fill="url(#bandMain)"/>
      <path d="M0,880 C300,860 600,840 900,820 L900,850 C600,880 300,910 0,950 Z" fill="#8fd3cf" opacity="0.7"/>
      <circle cx="790" cy="580" r="26" fill="#8fd3cf"/>
      <circle cx="848" cy="518" r="11" fill="#8fd3cf"/>
      <ellipse cx="865" cy="630" rx="36" ry="52" fill="#5fc2b9"/>
      <ellipse cx="30" cy="940" rx="28" ry="40" fill="#8fd3cf"/>
      <circle cx="80" cy="990" r="18" fill="#8fd3cf"/>
      <circle cx="40" cy="1030" r="8" fill="#8fd3cf"/>
    </svg>

    <header class="brand">
      <div class="brand-mark"></div>
      <div class="brand-name">ELORA BLOOM</div>
      <p class="tagline">Natural Nourishing<br>Australian Skin Care</p>
    </header>

    <h1 class="product-title">NATIVE<br>HYDRATING SERUM</h1>

    <section class="ingredients">
      <div class="ingredients-lead">With</div>
      <div class="ingredients-list">Quandong<span class="dot">•</span>Lilli Pilli<span class="dot">•</span>Kakadu Plum</div>
      <div class="skin-type">All Skin Types</div>
    </section>

    <footer class="base-band">
      <div class="net-weight">Net Wt.: <strong>30ml</strong></div>
      <div class="vegan-badge"></div>
    </footer>
  </div>
</body>
</html>
```